Business Card Design needed for logo design project

This project is linked to http://gigs.plumbfolio.net/task.aspx?id=472918
Kestrel Dues Partners.

Our company needs a Business Card Design. Please refer to our original project in the link above.

We would like the size to be a typical rectangle, no rounded edges or atypical sizes that will be costly to print. Thanks!

Target Market(s)

Small business owners in the U.S.

Industry/Entity Type

Business

```html
<!DOCTYPE html>
<html lang="en">
<head>
<meta charset="utf-8">
<title>Kestrel Dues Partners – Business Card</title>
<link rel="stylesheet" href="https://fonts.googleapis.com/css2?family=Lato:wght@400;700&display=swap">
<style>
  :root {
    --page-bg: #f3f2f4;
    --card-white: #ffffff;
    --card-panel: #edf1f5;
    --brand-blue: #2f5ea8;
    --divider: #4a4f57;
    --ink: #2b2b2b;
    --ink-soft: #50555c;
  }
  * { box-sizing: border-box; margin: 0; padding: 0; }
  html, body {
    width: 1089px;
    height: 1200px;
    overflow: hidden;
    background: var(--page-bg);
    font-family: "Lato", sans-serif;
  }
  .canvas {
    position: relative;
    width: 1089px;
    height: 1200px;
  }
  .business-card {
    position: absolute;
    left: 94px;
    top: 350px;
    width: 900px;
    height: 500px;
    display: flex;
    box-shadow: 0 2px 10px rgba(0,0,0,0.06);
  }
  .card-side-white {
    width: 300px;
    background: var(--card-white);
  }
  .card-side-panel {
    flex: 1;
    background: var(--card-panel);
  }
  .brand-mark {
    position: absolute;
    left: 140px;
    top: 106px;
    width: 72px;
    height: 72px;
    background: var(--brand-blue);
  }
  .brand-divider {
    position: absolute;
    left: 296px;
    top: 80px;
    width: 3px;
    height: 114px;
    background: var(--divider);
  }
  .brand-name {
    position: absolute;
    left: 316px;
    top: 92px;
    font-size: 38px;
    font-weight: 400;
    line-height: 1.3;
    letter-spacing: 0.5px;
    text-transform: uppercase;
    color: var(--brand-blue);
  }
  .contact-block {
    position: absolute;
    left: 316px;
    top: 290px;
    color: var(--ink);
  }
  .person-name {
    font-size: 24px;
    font-weight: 700;
    line-height: 1.2;
  }
  .person-title {
    font-size: 19px;
    color: var(--ink-soft);
    margin-top: 3px;
  }
  .contact-lines {
    margin-top: 34px;
    font-size: 19px;
    color: var(--ink-soft);
    line-height: 1.6;
  }
</style>
</head>
<body>
  <main class="canvas">
    <article class="business-card">
      <div class="card-side-white"></div>
      <div class="card-side-panel"></div>

      <span class="brand-mark"></span>
      <span class="brand-divider"></span>
      <p class="brand-name">Kestrel Dues<br>Partners</p>

      <div class="contact-block">
        <p class="person-name">prename name</p>
        <p class="person-title">professional job title</p>
        <div class="contact-lines">
          <p>email: name.name@kestreldues.net</p>
          <p>mobile: 01632 960 418</p>
        </div>
      </div>
    </article>
  </main>
</body>
</html>
```